Thornwell Building Company - advertisement poster

I am looking to print some canvas signs to advertise my general contracting company, Thornwell Building Company. The sign will measure 6' long x 3' high so the size should match that ratio. I already have a logo icon, which is the Letter 'A' and some trees that I would like to incorporate, see attached. I would also like the to have the following information listed:
1) phone number: 472-318-6095
2) email: thornwellbuildingcompany@mailvistra.net
3) website: thornwellbuildingcompany.com
4) Lic#5386204
5) I want to use this text: "BUILD WITH THE T-CREW!"

The ad should be relatively simple and clean. Black and Green are my company colors. I am open to creative ideas!

Target Market(s)

People looking to renovate their homes

Industry/Entity Type

Construction

Colors
59FF00
82FF00
B8FF75
E3FFCB
F4FFEA

Requirements
Must have
• Must have my company logo
Should not have
• No photos or complex graphics

```html
<!DOCTYPE html>
<html lang="en">
<head>
<meta charset="utf-8">
<title>Thornwell Building Company – Build with the T-Crew</title>
<link rel="stylesheet" href="https://fonts.googleapis.com/css2?family=Montserrat:wght@800&family=Open+Sans:wght@400;700&display=swap">
<style>
  :root {
    --ink: #0a0a0a;
    --paper: #ffffff;
    --forest: #6fb14a;
    --haze-top: #f1f1f1;
    --haze-bottom: #e2e2e2;
  }
  * { margin: 0; padding: 0; box-sizing: border-box; }
  html, body { width: 1200px; height: 600px; overflow: hidden; background: var(--paper); }
  .poster {
    position: relative;
    width: 1200px;
    height: 600px;
    overflow: hidden;
    background: var(--paper);
  }
  .scene { position: absolute; inset: 0; width: 1200px; height: 600px; }
  .skyline-area { fill: url(#skylineTone); }
  .forest-area { fill: var(--forest); }
  .ground { fill: var(--ink); }

  .brand {
    position: absolute;
    top: 58px;
    right: 70px;
    display: flex;
    align-items: center;
    gap: 8px;
  }
  .brand-mark { width: 14px; height: 14px; background: var(--forest); }
  .brand-name {
    font-family: "Montserrat", sans-serif;
    font-weight: 800;
    font-size: 14px;
    line-height: 1.15;
    color: var(--ink);
    text-transform: uppercase;
    letter-spacing: 0.5px;
  }

  .headline {
    position: absolute;
    left: 0;
    width: 1200px;
    text-align: center;
    font-family: "Montserrat", sans-serif;
    font-weight: 800;
    font-size: 59px;
    line-height: 1;
    letter-spacing: 1px;
  }
  .headline-lead { top: 120px; color: var(--ink); }
  .headline-crew { top: 342px; color: var(--paper); }

  .contact {
    position: absolute;
    left: 0;
    top: 420px;
    width: 1200px;
    text-align: center;
    font-family: "Open Sans", sans-serif;
    color: var(--paper);
  }
  .contact-phone { font-weight: 700; font-size: 41px; line-height: 48px; }
  .contact-line { font-weight: 400; font-size: 21px; line-height: 26.5px; }
</style>
</head>
<body>
<main class="poster">
  <svg class="scene" viewBox="0 0 1200 600" aria-hidden="false">
    <defs>
      <linearGradient id="skylineTone" x1="0" y1="0" x2="0" y2="1">
        <stop offset="0" stop-color="var(--haze-top)"/>
        <stop offset="1" stop-color="var(--haze-bottom)"/>
      </linearGradient>
    </defs>
    <rect class="skyline-area" role="img" aria-label="Silhouettes of tower cranes and a building under construction"
          x="68" y="30" width="1092" height="390"/>
    <polygon class="forest-area" role="img" aria-label="Row of green pine trees rising toward the centre"
             points="0,420 70,382 145,350 220,318 295,286 370,254 445,222 520,190 680,190 755,222 830,254 905,286 980,318 1055,350 1130,382 1200,410 1200,524 0,524"/>
    <polygon class="ground"
             points="478,303 722,303 722,335 797,335 797,366 873,366 873,398 949,398 949,430 1024,430 1024,462 1100,462 1100,493 1175,493 1175,524 1200,524 1200,600 0,600 0,524 25,524 25,493 100,493 100,462 176,462 176,430 251,430 251,398 327,398 327,366 403,366 403,335 478,335"/>
  </svg>

  <div class="brand">
    <span class="brand-mark"></span>
    <span class="brand-name">Thornwell<br>Building Company</span>
  </div>

  <h1 class="headline headline-lead">BUILD WITH THE</h1>
  <p class="headline headline-crew">T-CREW</p>

  <section class="contact">
    <p class="contact-phone">472-318-6095</p>
    <p class="contact-line">email: thornwellbuildingcompany@mailvistra.net</p>
    <p class="contact-line">thornwellbuildingcompany.com</p>
    <p class="contact-line">Lic# 5386204</p>
  </section>
</main>
</body>
</html>
```